Popup Nightclub Grand Opening Flyer

We need to design a flyer for the grand opening of an upscale, exclusive nightclub called "Lanternfall". The design needs to be chic and exclusive. The background should be black and the text should primarily be white. We like minimalist designs.

Here is the text for the flyer
-
Velvetrope Atlanta Presents

Lanternfall (LOGO)

A Popup Nightclub Experience
For one night Only

Friday, October 18, 2013
Party begins at 9PM

INVITE ONLY

See invitation for location details
(Velvetrope Atlanta logo)

-
Examples we like

http://cdn2-b.brivelpost.com/sites/default/files/styles/image_content_width/hash/3d/fa/1472093815_4471_flyer.jpg?itok=R8kqWm2z

http://api.plovra.com/files/7Kqq-Tr82XXB3pQzJvmtR5HL2W719E4nbRtC6KLd4HsfM8Y2qTDK-VmjwDoNqLX4QBzTHD9nakRbVx3m-Pfq8htc3MDTWr5p4/2zelSaturdays.jpg

http://quenmar.com/wp-content/uploads/yootheme/widgetkit/gallery/2zel/2zel-gen_vroom4-01.jpg

Hi All, one thing that we are seeing that we don't like is on over emphasis on the phrase "a popup nightclub experience" please don't make this the largest thing on the flyer

Target Market(s)

Target market is 25-35 year olds who are affluent (rich) and like luxury brands

Requirements
Must have
• Dark Background
Nice to have
• Velvetrope Logo on the bottom
Modern text that isn't curvy
Should not have
• Curved text

```html
<!DOCTYPE html>
<html lang="en">
<head>
<meta charset="utf-8">
<title>Lanternfall Nightclub – Popup Night</title>
<link rel="stylesheet" href="https://fonts.googleapis.com/css2?family=Graduate&family=Josefin+Sans:wght@300;400&display=swap">
<style>
  :root {
    --ink: #f4f4f4;
    --silver: #d6d6d6;
    --rule: #a9a9a9;
    --bg-center: #262626;
    --bg-edge: #050505;
  }
  html, body {
    margin: 0;
    padding: 0;
    overflow: hidden;
    background: var(--bg-edge);
  }
  .flyer {
    position: relative;
    width: 900px;
    height: 1200px;
    overflow: hidden;
    background: radial-gradient(ellipse 70% 60% at 50% 45%, var(--bg-center) 0%, #141414 55%, var(--bg-edge) 100%);
    color: var(--ink);
    text-align: center;
  }
  .slab {
    font-family: "Graduate", "Rockwell", serif;
    text-transform: uppercase;
  }
  .sans {
    font-family: "Josefin Sans", "Helvetica Neue", sans-serif;
    text-transform: uppercase;
  }
  .presenter {
    position: absolute;
    top: 34px;
    left: 0;
    width: 100%;
    font-size: 23px;
    letter-spacing: 9px;
    margin: 0;
  }
  .brand-mark {
    position: absolute;
    top: 148px;
    left: 365px;
    width: 170px;
    height: 170px;
  }
  .brand-name {
    position: absolute;
    top: 392px;
    left: 0;
    width: 100%;
    margin: 0;
    font-weight: 300;
    font-size: 74px;
    letter-spacing: 9px;
    line-height: 1;
    color: var(--ink);
  }
  .brand-name .venue-type {
    display: block;
    margin-top: 22px;
    font-size: 40px;
    letter-spacing: 5px;
  }
  .rule {
    position: absolute;
    left: 62px;
    width: 772px;
    height: 5px;
    border-radius: 3px;
    background: var(--rule);
  }
  .rule.upper { top: 575px; }
  .rule.lower { top: 800px; }
  .tagline {
    position: absolute;
    top: 604px;
    left: 0;
    width: 100%;
    margin: 0;
    font-size: 25px;
    letter-spacing: 5px;
    line-height: 36px;
  }
  .when {
    position: absolute;
    top: 704px;
    left: 0;
    width: 100%;
    margin: 0;
    font-weight: 400;
    font-size: 31px;
    letter-spacing: 5px;
    line-height: 43px;
  }
  .access {
    position: absolute;
    top: 842px;
    left: 0;
    width: 100%;
    margin: 0;
    font-size: 62px;
    letter-spacing: 8px;
    line-height: 1;
  }
  .location-note {
    position: absolute;
    top: 972px;
    left: 0;
    width: 100%;
    margin: 0;
    font-weight: 400;
    font-size: 30px;
    letter-spacing: 5px;
    line-height: 40px;
  }
  .host-sign {
    position: absolute;
    top: 1124px;
    left: 0;
    width: 100%;
    display: flex;
    justify-content: center;
    align-items: center;
    gap: 14px;
  }
  .host-sign .dot {
    width: 30px;
    height: 30px;
    border-radius: 50%;
    background: var(--silver);
  }
  .host-sign .host-name {
    font-weight: 400;
    font-size: 26px;
    letter-spacing: 3px;
    color: var(--ink);
    padding-top: 4px;
  }
</style>
</head>
<body>
  <main class="flyer">
    <p class="presenter slab">Velvetrope Atlanta Presents</p>

    <svg class="brand-mark" viewBox="0 0 170 170" aria-hidden="true">
      <circle cx="85" cy="85" r="85" fill="var(--silver)"/>
    </svg>

    <h1 class="brand-name sans">Lanternfall<span class="venue-type">Nightclub</span></h1>

    <div class="rule upper"></div>

    <p class="tagline slab">A Popup Nightclub Experience<br>For One Night Only</p>

    <p class="when sans">Friday, October 18, 2013<br>Party Begins at 9PM</p>

    <div class="rule lower"></div>

    <h2 class="access slab">Invite Only</h2>

    <p class="location-note sans">See Invitation<br>For Location Details</p>

    <div class="host-sign">
      <span class="dot"></span>
      <span class="host-name sans">Velvetrope Atlanta</span>
    </div>
  </main>
</body>
</html>
```